Web Design Project- eLearning Company

Hello Designers,
We just successfully used pixel-forge to design the logo of our new company, and would like to now accept submissions for design of our website. We have seen several creative designs out there in pixelforge, and hope to use your skills to develop a highly professional site that sets us apart and quickly conveys our offering to the viewer.
About the Company: Vendaroo is a new eLearning company, based in India. We plan to develop and offer complete eLearning solutions to companies in India. Please note that we are not targeting consumers or students. Our website will be viewed by middle management/senior management executives of large companies and needs to have a look-n-feel that establishes ourselves as a leader in this space.
What do we offer? We aim to offer a complete eLearning solution that will enable our customer to roll-out and execute an eLearning program for its employees, field sales teams, business ecosystem (resellers/distributors), brand franchisees or dealers.
Components of our offering: In order to be a one-stop shop for our customer, we offer all the components required for them to successfully roll out a Learning program. The homepage *needs to showcase * this.
This includes -
(1) the technology platform (LMS or Learning Management System) which hosts the content and provides administrative features and maintains database of learning records, scores etc.. See quendrix.example for a view on how these work.
(2) the actual learning content that we will develop for them. We will build a library of generic content, but initially the emphasis should be on custom content development. This includes interactive course material and assessments. See morvela.example or tessubrook.example for this.
(3) administrative services to help customers plan, execute and collect data. We will offer helpdesk services to learners and training administrators so that client does not waste time and efforts in driving this initiative- We will manage it for them. The following link shows another company's similar service offering:
http://www.brightholm.example/services/Learning-Services/Learning-Operations/Learning-Support-Services
The Job:
We need a home page, as well as the following pages to be designed:
1. HomePage
2. About Us
3. Products and Services
4. News & Blog
5. Contact us
Design guidelines:
-Colors:I have uploaded our corporate logo. Either the logo colors can be used, or the color theme needs to be in harmony with the logo colors. I would like to see different styles before we can begin to narrow down on a particular style. Having a slider at the top with 3-4 slides would be worth checking out.
Content:
-Home Page: Slider, a client testimonial box, a graphic that showcases our 3-pillar offering (Platform+ content + administrative services) and a box showcasing the latest news release. Designers are welcome to stray from this and present alternate designs. In fact, we encourage you to be creative.
- Other pages- Similar to any standard corporate site.
- All Pages have to be SEO friendly.
CMS- Drupal/Joomla
Updates
websites that are worth looking into to get a feel of the breadth of our offering, and the look we aim for:
glimmerpath.example
brightholm.example
Hello Designers,
We would love to receive more designs from all of you. So far, none of the designs have hit the right buttons, the contest is therefore wide open and completely up for grabs !
As an update, we have now committed on the project funds, as we are confident that by the end of the content we will have a design that we can take to production.
Do feel free to shoot me any questions, concerns or suggestions that you may have. We will respond to all queries.
Cheers and Happy Designing !
Hello Designers,
The original content closing date is tomorrow (Saturday). If there are designers that are working on designs and need more time, then please let me know so that I can extend the deadline.
I encourage you to actively participate, the contest is still open.
Thanks.
I have added another image file that has our company logo done in a stylized fashion. You were welcome to use this as well.

```html
<!DOCTYPE html>
<html lang="en">
<head>
<meta charset="utf-8">
<title>Vendaroo – eLearning for Business Outcomes</title>
<link href="https://fonts.googleapis.com/css2?family=Source+Sans+3:wght@400;600;700&display=swap" rel="stylesheet">
<style>
:root{
  --green:#7ab51d;
  --green-dark:#6aa012;
  --charcoal:#3e4348;
  --ink:#222;
  --text:#4a4a4a;
  --muted:#888;
  --panel:#f2f2f2;
  --line:#d6d6d6;
  --white:#fff;
  --accent:#e8661a;
}
*{box-sizing:border-box;margin:0;padding:0}
html,body{width:1130px;height:1200px;overflow:hidden}
body{font-family:"Source Sans 3",sans-serif;color:var(--text);background:var(--white);position:relative}
a{color:inherit;text-decoration:none}

.top-rule{height:4px;background:var(--green)}
.site-header{position:relative;height:134px}
.signup{position:absolute;left:850px;top:0;width:146px;height:28px;background:var(--green);color:var(--white);font-weight:700;font-size:12.5px;display:flex;align-items:center;justify-content:center;border-radius:0 0 3px 3px}
.brand{position:absolute;left:122px;top:38px;display:flex;align-items:center;gap:12px}
.brand-mark{width:56px;height:56px;border-radius:50%;background:var(--green)}
.brand-name{font-size:40px;font-weight:700;color:var(--charcoal);line-height:1}
.brand-tagline{font-size:11px;font-weight:600;color:var(--charcoal);margin-top:2px}
.search{position:absolute;left:844px;top:55px;display:flex;align-items:center;gap:8px}
.search-field{width:137px;height:30px;border:1px solid #d8d8d8;border-radius:2px;background:#f4f4f4;font-size:12px;color:#aaa;padding:0 8px;display:flex;align-items:center}

.main-nav{height:55px;background:var(--charcoal);position:relative}
.main-nav ul{list-style:none;position:absolute;left:134px;top:15px;display:flex;align-items:center;gap:0}
.main-nav li{font-size:14px;color:#e6e6e6;margin-right:38px}
.main-nav li.current{background:var(--green);color:var(--white);font-weight:600;padding:3px 10px;border-radius:2px;margin-right:28px}
.social{position:absolute;left:922px;top:18px;display:flex;gap:12px}
.social span{width:18px;height:18px;border-radius:50%;background:#e6e6e6}

.hero{position:relative;height:388px;background:linear-gradient(90deg,#eceeed 0%,#dfe2e1 45%,#cfd3d3 70%,#c4c7c6 100%);overflow:hidden}
.hero-photo{position:absolute;right:0;top:0;width:420px;height:388px;background:radial-gradient(ellipse at 55% 45%,#8a6a55 0%,#5b4438 28%,#6e7378 52%,rgba(200,203,203,0) 78%)}
.hero-copy{position:absolute;left:121px;top:73px;width:520px}
.hero h1{font-size:32px;font-weight:700;line-height:37px;color:#111;letter-spacing:.2px}
.hero p{font-size:14px;line-height:22px;color:#666;width:450px;margin-top:14px}
.hero-actions{display:flex;gap:7px;margin-top:17px}
.btn{height:44px;display:flex;align-items:center;justify-content:center;color:var(--white);font-weight:700;font-size:15px;border-radius:2px}
.btn-primary{width:173px;background:var(--green)}
.btn-dark{width:197px;background:var(--charcoal)}
.slider-dots{display:flex;gap:8px;margin-top:20px}
.slider-dots i{width:12px;height:12px;border-radius:50%;background:#666}
.slider-dots i.active{background:var(--green)}

.pillars{position:relative;height:260px}
.pillar{position:absolute;top:23px;width:260px}
.pillar:nth-child(1){left:120px}
.pillar:nth-child(2){left:436px}
.pillar:nth-child(3){left:751px}
.pillar-head{display:flex;align-items:center;gap:12px}
.pillar-icon{width:62px;height:62px;border-radius:50%;background:#f6f6f6;border:1px solid #e2e2e2;box-shadow:inset 0 0 0 4px #fff;display:flex;align-items:center;justify-content:center;flex:none}
.pillar h2{font-size:22px;font-weight:700;color:var(--green);letter-spacing:.3px}
.pillar p{font-size:12.3px;line-height:17px;color:#444;text-align:justify;margin-top:14px;height:82px}
.learn-more{display:flex;justify-content:flex-end;align-items:center;gap:10px;font-size:13.5px;color:#444;margin-top:37px}
.learn-more b{width:18px;height:18px;background:var(--charcoal);display:flex;align-items:center;justify-content:center}

.feed{position:relative;height:310px;background:var(--panel)}
.feed h3{position:absolute;top:27px;font-size:21px;font-weight:400;color:var(--ink)}
.news{position:absolute;left:122px;top:0;width:260px}
.news h3{left:0}
.news h4{position:absolute;top:74px;font-size:17px;font-weight:600;color:#333;white-space:nowrap}
.news time{position:absolute;top:100px;font-size:13px;color:var(--muted)}
.news time sup{font-size:8px}
.news p{position:absolute;top:132px;width:262px;font-size:12.5px;line-height:21.7px;color:#444}
.news .more{position:absolute;top:252px;font-size:12.5px;letter-spacing:.5px;color:#777;white-space:nowrap}
.tweets h3{left:414px}
.tweet-list{position:absolute;left:412px;top:73px;width:258px;height:206px;border:1px solid var(--line);background:#f6f6f6}
.tweet{padding:14px 17px 0;font-size:12.3px;line-height:19px;color:#333}
.tweet:first-child{height:94px;border-bottom:1px solid var(--line)}
.tweet .handle{color:#888}
.tweet small{display:block;font-size:10.5px;color:#888;margin-top:8px}
.clients h3{left:695px}
.client-dots{position:absolute;left:979px;top:111px;display:flex;gap:3px}
.client-dots i{width:5px;height:5px;border-radius:50%;background:#ccc}
.client-dots i.active{background:#555}
.quote{position:absolute;left:690px;top:73px;width:317px;height:166px;background:var(--white);border:1px solid var(--line);box-shadow:0 2px 0 #ddd;padding:28px 28px 0 32px;font-size:12.3px;line-height:21.7px;color:#333}
.quote-mark{position:absolute;right:16px;bottom:14px;font-size:30px;font-weight:700;color:#333;line-height:1;font-family:Georgia,serif}
.quote-tail{position:absolute;left:292px;bottom:-10px;width:18px;height:18px;background:var(--white);border-right:1px solid var(--line);border-bottom:1px solid var(--line);transform:rotate(45deg)}
.attribution{position:absolute;right:127px;top:253px;font-size:12.5px;color:#333}
.attribution strong{font-weight:600}
.attribution .company{color:var(--accent);font-weight:600}

.site-footer{height:49px;background:var(--charcoal);color:#eee;font-size:12.3px;display:flex;align-items:center;justify-content:space-between;padding:0 130px 0 125px}
.site-footer ul{list-style:none;display:flex}
.site-footer li+li::before{content:"|";margin:0 14px}
</style>
</head>
<body>
<div class="top-rule"></div>
<header class="site-header">
  <a class="signup" href="#">SIGN UP NOW!</a>
  <a class="brand" href="#">
    <span class="brand-mark"></span>
    <span>
      <span class="brand-name">Vendaroo</span>
      <span class="brand-tagline" style="display:block">eLearning for Business Outcomes.</span>
    </span>
  </a>
  <form class="search" role="search">
    <span class="search-field">search</span>
    <svg width="17" height="17" viewBox="0 0 17 17" aria-hidden="true"><circle cx="7" cy="7" r="5.3" fill="none" stroke="#111" stroke-width="2.2"/><line x1="11" y1="11" x2="15.5" y2="15.5" stroke="#111" stroke-width="2.6" stroke-linecap="round"/></svg>
  </form>
</header>

<nav class="main-nav">
  <ul>
    <li class="current">Home</li>
    <li>About Us</li>
    <li>Products</li>
    <li>News &amp; Blog</li>
    <li>Contact Us</li>
  </ul>
  <div class="social" aria-label="Social links"><span></span><span></span><span></span></div>
</nav>

<section class="hero">
  <div class="hero-photo" role="img" aria-label="Photo of a smiling businesswoman working at a laptop in a bright office"></div>
  <div class="hero-copy">
    <h1>WE OFFER COMPLETE ELEARNING SOLUTIONS TO COMPANIES</h1>
    <p>Contrairement à une opinion répandue, le Lorem Ipsum n'est pas simplement du texte aléatoire. Il trouve ses racines dans une oeuvre de la littérature latine classique datant de..</p>
    <div class="hero-actions">
      <a class="btn btn-primary" href="#">SEE OUR PRICING</a>
      <a class="btn btn-dark" href="#">START LEARNING TODAY</a>
    </div>
    <div class="slider-dots"><i></i><i></i><i class="active"></i></div>
  </div>
</section>

<section class="pillars">
  <article class="pillar">
    <div class="pillar-head">
      <span class="pillar-icon"><svg width="46" height="46" viewBox="0 0 46 46" aria-hidden="true"><circle cx="23" cy="23" r="22" fill="var(--charcoal)"/><path d="M16 31 L18 25 L29 14 L33 18 L22 29 Z" fill="#fff"/><path d="M16 31 L18 25 L22 29 Z" fill="var(--charcoal)" stroke="#fff" stroke-width="1"/></svg></span>
      <h2>PLATFORM</h2>
    </div>
    <p>Facial expression contains a huge amount of information concerning emotion, mental states and intentions. Mood Meter quantifies the expression in naturalistic behaviour, providing invaluable insight into human behaviour.</p>
    <a class="learn-more" href="#">Learn More <b><svg width="8" height="10" viewBox="0 0 8 10"><path d="M1 1 L6 5 L1 9" fill="none" stroke="#fff" stroke-width="2"/></svg></b></a>
  </article>
  <article class="pillar">
    <div class="pillar-head">
      <span class="pillar-icon"><svg width="46" height="46" viewBox="0 0 46 46" aria-hidden="true" fill="var(--charcoal)"><circle cx="23" cy="23" r="8"/><path d="M17 3 H29 L23 11 Z"/><path d="M17 43 H29 L23 35 Z"/><path d="M3 17 V29 L11 23 Z"/><path d="M43 17 V29 L35 23 Z"/></svg></span>
      <h2>CONTENT</h2>
    </div>
    <p>Gaze is an important factor in human interactions and very useful in determining a person's focus of attention. Mood Meter enables accurate eye tracking for use in analysis of gaze. This is useful for the design of HCI and safety critical systems.</p>
    <a class="learn-more" href="#">Learn More <b><svg width="8" height="10" viewBox="0 0 8 10"><path d="M1 1 L6 5 L1 9" fill="none" stroke="#fff" stroke-width="2"/></svg></b></a>
  </article>
  <article class="pillar">
    <div class="pillar-head">
      <span class="pillar-icon"><svg width="46" height="46" viewBox="0 0 46 46" aria-hidden="true"><g fill="var(--charcoal)" transform="translate(23 23)"><rect x="-4" y="-21" width="8" height="10"/><rect x="-4" y="-21" width="8" height="10" transform="rotate(45)"/><rect x="-4" y="-21" width="8" height="10" transform="rotate(90)"/><rect x="-4" y="-21" width="8" height="10" transform="rotate(135)"/><rect x="-4" y="-21" width="8" height="10" transform="rotate(180)"/><rect x="-4" y="-21" width="8" height="10" transform="rotate(225)"/><rect x="-4" y="-21" width="8" height="10" transform="rotate(270)"/><rect x="-4" y="-21" width="8" height="10" transform="rotate(315)"/><circle r="15"/></g><circle cx="23" cy="23" r="6" fill="#f6f6f6"/></svg></span>
      <h2>ADMINISTRATION</h2>
    </div>
    <p>A person interacting with a product is as much emotional as it is rational. Mood Meter can quantify facial behaviour to understand how a consumer responds to a product prototype or advertising in the development phase.</p>
    <a class="learn-more" href="#">Learn More <b><svg width="8" height="10" viewBox="0 0 8 10"><path d="M1 1 L6 5 L1 9" fill="none" stroke="#fff" stroke-width="2"/></svg></b></a>
  </article>
</section>

<section class="feed">
  <div class="news">
    <h3>Latest News</h3>
    <h4>Lorem ipsum dolor sit amet</h4>
    <time>14<sup>th</sup> November</time>
    <p>Nam libero tempore, cum soluta nobis est eligendi optio cumque nihil impedit quo lorem ipsum dolor sit minus id quod maxime placeat facere possimus, omnis voluptas assumenda est, omnis dolor repellendus...</p>
    <a class="more" href="#">FULL ARTICLE &nbsp;›</a>
  </div>
  <div class="tweets">
    <h3>Recent Tweets</h3>
    <div class="tweet-list">
      <div class="tweet"><span class="handle">@quietfern</span> Lorem ipsum dolor sit amet consectetur adipisicing elit.<small>9 hours ago</small></div>
      <div class="tweet"><span class="handle">@tallbirch</span> At vero eos et accusamus et iusto odio dignissimos ducimus blanditiis praesentium voluptatum<small>1 day ago</small></div>
    </div>
  </div>
  <div class="clients">
    <h3>Our Client’s are Awesome</h3>
    <div class="client-dots"><i></i><i></i><i class="active"></i></div>
    <blockquote class="quote">At vero eos et accusamus et lucero iusto odio dignissimos ducimus qui blanditiis praesentium voluptatum deleniti atque corrupti quos dolores et quas molestias excepturi sint occaecati cupiditate non provident.<span class="quote-mark">”</span><span class="quote-tail"></span></blockquote>
    <p class="attribution"><strong>John Doe</strong>, <span class="company">xyz etc.</span>, cat lover</p>
  </div>
</section>

<footer class="site-footer">
  <ul><li>Home</li><li>About Us</li><li>Products</li><li>News &amp; Blog</li><li>Contact Us</li></ul>
  <span>Copyright©2013 Vendaroo. All Rights Reserved</span>
</footer>
</body>
</html>
```